Corrindale Planners, LLC Stationary

Corrindale Planners, LLC is a new financial planning and consulting company. We are looking for designs on business cards, letterhead, envelopes, and anything else that would be useful. Our preference for business card design is two sided. We are looking for a professional and clean look with incorporating the logo and patriotic feel. Thank you to all who participate and good luck!

```html
<!DOCTYPE html>
<html lang="en">
<head>
<meta charset="utf-8">
<title>Corrindale Planners, LLC Stationery</title>
<link href="https://fonts.googleapis.com/css2?family=Open+Sans:wght@400;600&display=swap" rel="stylesheet">
<style>
:root{
  --navy:#0d3f6b;
  --red:#c8202f;
  --ink:#1c2b3a;
  --paper:#ffffff;
  --backdrop:#b5b5b5;
  --faint-navy:#e4e8ed;
  --faint-red:#f6e3e5;
}
*{margin:0;padding:0;box-sizing:border-box}
html,body{width:1200px;height:960px;overflow:hidden}
body{background:var(--backdrop);font-family:"Open Sans",Arial,sans-serif;color:var(--ink);position:relative}
.sheet{position:absolute;background:var(--paper);box-shadow:8px 10px 12px rgba(0,0,0,.35);overflow:hidden}
.wordmark{font-weight:600;color:var(--navy);text-transform:uppercase;letter-spacing:.04em;line-height:1.1;display:flex;align-items:center;gap:6px;white-space:nowrap}
.wordmark .dot{width:10px;height:10px;border-radius:50%;background:var(--red);flex:none}
.contact{list-style:none;line-height:1.45}
.contact li{display:flex;align-items:center;gap:5px;white-space:nowrap}
.contact svg{flex:none}
.address{color:var(--navy);line-height:1.25;white-space:nowrap}
.holder-name{font-weight:600;color:var(--navy)}
.role{color:var(--ink)}
.emblem-area{position:absolute;border-radius:50%}

/* letterhead */
.letterhead{left:54px;top:54px;width:459px;height:594px}
.letterhead .wordmark{position:absolute;left:45px;top:50px;font-size:12px}
.letterhead .contact-block{position:absolute;left:329px;top:30px;border-left:1px solid var(--navy);padding-left:8px;font-size:6px}
.letterhead .emblem-area{left:240px;top:380px;width:220px;height:220px;background:var(--faint-navy)}

/* cards */
.card{width:273px;height:156px}
.card-navy{left:554px;top:54px;background:var(--navy);color:#fff}
.card-navy .holder-name,.card-navy .role,.card-navy .address{color:#fff}
.card-navy .info{position:absolute;left:16px;top:20px;font-size:8.5px}
.card-navy .emblem-area{left:160px;top:35px;width:100px;height:100px;background:#fff}
.card-split{left:866px;top:54px}
.card-split .info{position:absolute;left:16px;top:18px;font-size:8.5px}
.card-split .emblem-area{left:30px;top:60px;width:70px;height:70px;background:var(--navy)}
.card-split .contact-block{position:absolute;left:129px;top:62px;border-left:1px solid var(--navy);padding-left:14px;height:76px;font-size:8.5px}
.card-side{left:554px;top:235px;width:275px;height:158px}
.card-side .emblem-area{left:-60px;top:40px;width:150px;height:150px;background:var(--navy)}
.card-side .info{position:absolute;left:145px;top:18px;font-size:8.5px}
.card-brand{left:866px;top:235px;width:275px;height:158px}
.card-brand .wordmark{position:absolute;left:0;right:0;top:70px;justify-content:center;font-size:15px}

/* compliments slip */
.slip{left:554px;top:445px;width:422px;height:198px}
.slip .heading{position:absolute;right:16px;top:10px;font-size:11px;color:var(--navy)}
.slip .emblem-area{left:255px;top:40px;width:150px;height:150px;background:var(--faint-navy)}
.slip .wordmark{position:absolute;left:20px;top:164px;font-size:10px}

/* envelopes */
.env-front{left:54px;top:689px;width:467px;height:234px}
.env-front .wordmark{position:absolute;left:18px;top:22px;font-size:9px}
.env-front .address{position:absolute;left:16px;top:46px;font-size:6px}
.env-front .emblem-area{left:290px;top:70px;width:160px;height:160px;background:var(--faint-navy)}
.env-back{left:554px;top:689px;width:522px;height:236px}
.env-back .flap{position:absolute;left:0;top:0;width:522px;height:72px}
.env-back .wordmark{position:absolute;left:0;right:0;top:30px;justify-content:center;font-size:9px}
</style>
</head>
<body>

<svg width="0" height="0" style="position:absolute">
  <defs>
    <symbol id="i-mobile" viewBox="0 0 10 10"><rect x="3" y="1" width="4" height="8" rx="0.8" fill="none" stroke="currentColor" stroke-width="1"/></symbol>
    <symbol id="i-phone" viewBox="0 0 10 10"><path d="M3 1.5 Q1.5 5 5 8.5 L6.5 7.5 L5.5 6.2 L4.6 6.6 Q3.4 5.2 3.6 3.8 L4.6 3.3 L4.2 1.5 Z" fill="currentColor"/></symbol>
    <symbol id="i-mail" viewBox="0 0 10 10"><rect x="1" y="2.5" width="8" height="5.5" fill="none" stroke="currentColor" stroke-width="1"/><path d="M1 2.5 L5 5.5 L9 2.5" fill="none" stroke="currentColor" stroke-width="1"/></symbol>
    <symbol id="i-web" viewBox="0 0 10 10"><circle cx="5" cy="5" r="3.8" fill="none" stroke="currentColor" stroke-width="1"/><path d="M1.2 5 H8.8 M5 1.2 V8.8" stroke="currentColor" stroke-width="0.8"/></symbol>
  </defs>
</svg>

<section class="sheet letterhead">
  <div class="wordmark"><span class="dot"></span>Corrindale Planners, LLC</div>
  <div class="contact-block">
    <ul class="contact" style="color:var(--red)">
      <li><svg width="7" height="7"><use href="#i-phone"/></svg><span style="color:var(--ink)">+1 555 018 7741</span></li>
      <li><svg width="7" height="7"><use href="#i-mail"/></svg><span style="color:var(--ink)">info@corrindale.com</span></li>
      <li><svg width="7" height="7"><use href="#i-web"/></svg><span style="color:var(--ink)">www.corrindale.com</span></li>
    </ul>
    <p class="address">480 Elm Ave, Suite 210<br>Westbrook, CA 91450</p>
  </div>
  <div class="emblem-area" role="img" aria-label="Faint brand emblem decoration"></div>
</section>

<section class="sheet card card-navy">
  <div class="info">
    <p class="holder-name" style="font-size:10px">Marcus Ellery</p>
    <p class="role">Director</p>
    <ul class="contact" style="margin-top:16px">
      <li><svg width="8" height="8"><use href="#i-mobile"/></svg>+1 555 014 2230</li>
      <li><svg width="8" height="8"><use href="#i-phone"/></svg>+1 555 018 7741</li>
      <li style="margin-top:5px"><svg width="8" height="8"><use href="#i-mail"/></svg>info@corrindale.com</li>
      <li><svg width="8" height="8"><use href="#i-web"/></svg>www.corrindale.com</li>
    </ul>
    <p class="address" style="margin-top:5px">480 Elm Ave, Suite 210<br>Westbrook, CA 91450</p>
  </div>
  <div class="emblem-area" role="img" aria-label="Brand emblem"></div>
</section>

<section class="sheet card card-split">
  <div class="info">
    <p class="holder-name" style="font-size:10px">Marcus Ellery</p>
    <p class="role">Director</p>
  </div>
  <div class="emblem-area" role="img" aria-label="Brand emblem"></div>
  <div class="contact-block">
    <ul class="contact" style="color:var(--red)">
      <li><svg width="8" height="8"><use href="#i-mobile"/></svg><span style="color:var(--ink)">+1 555 014 2230</span></li>
      <li><svg width="8" height="8"><use href="#i-phone"/></svg><span style="color:var(--ink)">+1 555 018 7741</span></li>
      <li style="margin-top:4px"><svg width="8" height="8"><use href="#i-mail"/></svg><span style="color:var(--ink)">info@corrindale.com</span></li>
      <li><svg width="8" height="8"><use href="#i-web"/></svg><span style="color:var(--ink)">www.corrindale.com</span></li>
    </ul>
    <p class="address" style="margin-top:4px">480 Elm Ave, Suite 210<br>Westbrook, CA 91450</p>
  </div>
</section>

<section class="sheet card card-side">
  <div class="emblem-area" role="img" aria-label="Brand emblem"></div>
  <div class="info">
    <p class="holder-name" style="font-size:10px">Marcus Ellery</p>
    <p class="role">Director</p>
    <ul class="contact" style="margin-top:16px;color:var(--red)">
      <li><svg width="8" height="8"><use href="#i-mobile"/></svg><span style="color:var(--ink)">+1 555 014 2230</span></li>
      <li><svg width="8" height="8"><use href="#i-phone"/></svg><span style="color:var(--ink)">+1 555 018 7741</span></li>
      <li style="margin-top:4px"><svg width="8" height="8"><use href="#i-mail"/></svg><span style="color:var(--ink)">info@corrindale.com</span></li>
      <li><svg width="8" height="8"><use href="#i-web"/></svg><span style="color:var(--ink)">www.corrindale.com</span></li>
    </ul>
    <p class="address" style="margin-top:5px">480 Elm Ave, Suite 210<br>Westbrook, CA 91450</p>
  </div>
</section>

<section class="sheet card card-brand">
  <div class="wordmark"><span class="dot"></span>Corrindale Planners, LLC</div>
</section>

<section class="sheet slip">
  <p class="heading">With Compliments</p>
  <div class="emblem-area" role="img" aria-label="Faint brand emblem decoration"></div>
  <div class="wordmark"><span class="dot" style="width:8px;height:8px"></span>Corrindale Planners, LLC</div>
</section>

<section class="sheet env-front">
  <div class="wordmark"><span class="dot" style="width:8px;height:8px"></span>Corrindale Planners, LLC</div>
  <p class="address">480 Elm Ave, Suite 210<br>Westbrook, CA 91450</p>
  <div class="emblem-area" role="img" aria-label="Faint brand emblem decoration"></div>
</section>

<section class="sheet env-back">
  <svg class="flap" viewBox="0 0 522 72" aria-hidden="true">
    <path d="M0 0 H522 L514 46 Q512 50 506 50 H16 Q10 50 8 46 Z" fill="#fff" stroke="#d6d6d6" stroke-width="1"/>
    <path d="M16 52 H506" stroke="#cfcfcf" stroke-width="2"/>
  </svg>
  <div class="wordmark"><span class="dot" style="width:8px;height:8px"></span>Corrindale Planners, LLC</div>
</section>

</body>
</html>
```